Template for Tolvik Advisory PowerPoint

We would like to create a new template for PowerPoint based on our current logo and graphic design guidelines. The template should reflect our corporate identity and be easy to use to create different kind of PowerPoint presentations for different kind of customers. The current design guideline that are attached reflect the "old" look of the PPT design and is only to be seen as a reference.
Tolvik Advisory is a Management consulting company working within both public and private sector. We focus on strategic business development and work in close cooperation with the customer to make sure it is the customer that will become the hero, our work is to support and guide them to the top.
The design should reflect a modern company working in close cooperation with our customers to help them innovate and describe their future business model, and also help them to reach that goal!
Words and taglines that we use. Passion for the future. The power of the organisation. Power of thoughts. Inspiration. Engagement.
What we have in mind is a modern, clean and elegant design based on our current logo. Tolvik Advisory is a Swedish Company working primarily on the Swedish market so the template must be possible to translate to Swedish (however the design can be done in english and be translated later)

Reason: I would like to extend the deadline to receive some more alternatives!

Reason: I'm out travelling and would like to extend the timeline to be able to choose the right design for our template. /Henrik

Target Market(s)

Our target market is within both private and public sector. Our main focus is CxO level executives within our clients organisation.

Industry/Entity Type

Management Consulting

Font styles to use
Sans Serif

Colors

Designer to choose colors to be used in the design.

Requirements
Must have
• A PPT template that contains both slides for traditional text and graphic. We like to work a lot with graphical presentations and try to limit the text on our slides to a minimum.
Nice to have
• Slides for different chapters within the presentation. Slides for powerful one-liners. Title slides. Thank you slides at the end.
Should not have
• Massive text....

```html
<!DOCTYPE html>
<html lang="en">
<head>
<meta charset="utf-8">
<title>Tolvik Advisory – Presentation Template</title>
<link href="https://fonts.googleapis.com/css2?family=Bebas+Neue&family=Raleway:wght@300;400;500&family=Open+Sans:wght@400&display=swap" rel="stylesheet">
<style>
:root{
  --stage:#6f6f6f;
  --paper:#fbfbfb;
  --paper-shade:#ececec;
  --ink:#1c1c1c;
  --muted:#555;
  --red:#d5143f;
  --black:#111;
  --rule:#9a9a9a;
  --label:#ffffff;
}
*{box-sizing:border-box;margin:0;padding:0}
html,body{width:1200px;height:928px;overflow:hidden;background:var(--stage)}
body{position:relative;font-family:"Raleway",sans-serif;color:var(--ink)}
h1,h2,h3{font-weight:400}
.slide{position:absolute;width:552px;height:390px;overflow:hidden;
  background:radial-gradient(ellipse at 50% 40%,var(--paper) 0%,var(--paper) 45%,var(--paper-shade) 100%);
  box-shadow:0 2px 6px rgba(0,0,0,.35)}
.slide--cover{left:29px;top:20px}
.slide--text{left:620px;top:20px}
.slide--icons{left:28px;top:476px}
.slide--compare{left:620px;top:476px}
.label{position:absolute;width:552px;text-align:center;font-family:"Open Sans",sans-serif;font-size:20px;color:var(--label)}
.label--cover{left:29px;top:427px}
.label--text{left:620px;top:427px}
.label--icons{left:28px;top:883px}
.label--compare{left:620px;top:883px}

.hero-photo{position:absolute;left:0;top:0;width:552px;height:200px;
  background:linear-gradient(160deg,#4d6f9e 0%,#88aee0 40%,#3a4a5c 70%,#2a3340 100%)}
.accent-bar{position:absolute;left:196px;width:160px}
.accent-bar--cover{top:200px;height:12px;background:var(--red)}
.accent-bar--top{top:0;height:20px;background:linear-gradient(var(--black) 0 50%,var(--red) 50% 100%)}

.brand{font-family:"Raleway",sans-serif;font-weight:400;color:var(--ink);white-space:nowrap}
.brand--cover{position:absolute;top:226px;left:0;width:552px;text-align:center;font-size:26px}
.footer-brand{position:absolute;left:22px;top:356px;font-size:9px}

.cover-title{position:absolute;top:272px;width:552px;text-align:center;font-family:"Bebas Neue",sans-serif;font-size:33px;letter-spacing:.3px}
.cover-sub{position:absolute;top:314px;width:552px;text-align:center;font-weight:300;font-size:13px;color:var(--red)}
.cover-url{position:absolute;top:360px;left:0;width:552px;display:flex;align-items:center;gap:12px;font-size:9px;color:var(--red)}
.cover-url::before,.cover-url::after{content:"";flex:1;height:1px;background:#777}

.slide-title{position:absolute;top:38px;width:552px;text-align:center;font-family:"Bebas Neue",sans-serif;font-size:34px}
.footer-url{position:absolute;top:356px;left:142px;width:270px;display:flex;align-items:center;gap:8px;font-size:6px;color:var(--red)}
.footer-url::before,.footer-url::after{content:"";flex:1;height:1px;background:var(--rule)}
.page-no{position:absolute;left:520px;top:354px;width:11px;height:11px;border-radius:50%;background:var(--red);color:#fff;font-size:6px;line-height:11px;text-align:center}

.body-copy{position:absolute;left:22px;top:90px;width:510px;font-size:5.6px;line-height:9.7px;color:var(--muted);text-align:justify}
.body-copy p{margin-bottom:9.7px}

.team-band{position:absolute;left:0;top:106px;width:552px;height:160px;
  background:linear-gradient(90deg,#2a2624 0%,#3b3431 35%,#231f1d 60%,#1a1818 100%)}
.feature{position:absolute;top:24px;width:126px;text-align:center;color:#fff}
.feature__icon{width:60px;height:60px;margin:0 auto;border-radius:50%;background:#fff;display:flex;align-items:center;justify-content:center}
.feature__title{margin-top:10px;font-family:"Bebas Neue",sans-serif;font-size:17px}
.feature__text{margin-top:2px;font-size:6px;line-height:8px;text-align:justify;text-align-last:center;padding:0 14px;color:#ddd}
.band-note{position:absolute;left:24px;top:277px;width:504px;font-size:5.6px;line-height:10px;text-align:center;color:var(--muted)}

.compare-col{position:absolute;top:100px;width:192px}
.compare-col--a{left:44px}
.compare-col--b{left:320px}
.compare-col__title{text-align:center;font-family:"Bebas Neue",sans-serif;font-size:18px}
.compare-col__sub{text-align:center;font-size:5.8px;color:var(--muted);margin-top:3px}
.point{position:relative;padding-left:11px;margin-top:24px}
.point:first-of-type{margin-top:26px}
.point svg{position:absolute;left:0;top:0}
.point__name{font-size:7.5px;color:var(--red)}
.point__text{font-size:5.6px;line-height:7.6px;color:var(--muted)}
</style>
</head>
<body>

<section class="slide slide--cover">
  <div class="hero-photo" role="img" aria-label="Upward view of glass office towers against a blue sky"></div>
  <div class="accent-bar accent-bar--cover"></div>
  <div class="brand brand--cover">Tolvik Advisory</div>
  <h1 class="cover-title">LOREM IPSUM IS SIMPLY DUMMY TEXT</h1>
  <p class="cover-sub">LOREM IPSUM IS SIMPLY DUMMY TEXT</p>
  <div class="cover-url">www.tolvikadvisory.se</div>
</section>
<div class="label label--cover">Cover Page</div>

<section class="slide slide--text">
  <div class="accent-bar accent-bar--top"></div>
  <h2 class="slide-title">LOREM IPSUM DOLAR</h2>
  <div class="body-copy">
    <p>Lorem ipsum is simply dummy text of the printing and typesetting industry. It has been the standard placeholder text ever since printers first took a galley of type and scrambled it to make a specimen book. It has survived many centuries and the leap into electronic typesetting, remaining essentially unchanged in use. It became popular again when sheets of transfer lettering carried its passages, and more recently with desktop publishing software that ships with sample versions of the text built in for designers to use. Today it still fills layouts, mockups and templates around the world while the real copy is being written.</p>
    <p>Contrary to popular belief, lorem ipsum is not simply random text. It has roots in a piece of classical Latin literature, making it more than two thousand years old. A professor of classics once looked up one of the more obscure words in a passage, and by going through the cites of the word in classical literature he discovered its undoubted source. The passage comes from a treatise on the theory of ethics, very popular during the Renaissance, written by a Roman orator and statesman. The first line of the familiar text comes from a single sentence in one of its sections, which was later cut apart and scrambled by an unknown typesetter to become the filler we know today across print and screen. It has since been copied into countless books, websites and slide templates.</p>
    <p>The standard chunk of lorem ipsum used since the early print era is reproduced below for those interested. Sections from the original work are also reproduced in their exact form, accompanied by English versions from a later translation, exactly as they appeared in print.</p>
    <p>It is a long established fact that a reader will be distracted by the readable content of a page when looking at its layout. The point of using lorem ipsum is that it has a more or less normal distribution of letters, making it look like readable English. Many web page editors now use it as their default model text, and a search for the phrase will uncover many sites still in their infancy. Various versions have evolved over the years, sometimes by accident, sometimes on purpose, with injected humour and the like.</p>
    <p>There are many variations of passages of lorem ipsum available, but the majority have suffered alteration in some form, by injected humour or randomised words which do not look even slightly believable. If you are going to use a passage, you need to be sure there is nothing hidden in the middle of the text. All the generators on the web tend to repeat predefined chunks as necessary, making this the first true generator of its kind. It uses a dictionary of over two hundred Latin words, combined with a handful of model sentence structures, to generate text which looks reasonable and is therefore always free from repetition, injected humour or odd words.</p>
  </div>
  <div class="brand footer-brand">Tolvik Advisory</div>
  <div class="footer-url">www.tolvikadvisory.se</div>
  <div class="page-no">1</div>
</section>
<div class="label label--text">Page 01</div>

<section class="slide slide--icons">
  <div class="accent-bar accent-bar--top"></div>
  <h2 class="slide-title">LOREM IPSUM DOLAR</h2>
  <div class="team-band" role="img" aria-label="Dark-toned photo of business colleagues in a meeting">
    <div class="feature" style="left:25px">
      <div class="feature__icon"><svg width="24" height="20" viewBox="0 0 24 20"><g fill="#d5143f"><rect x="0" y="15" width="2" height="5"/><rect x="4" y="13" width="2" height="7"/><rect x="8" y="11" width="2" height="9"/><rect x="12" y="9" width="2" height="11"/><rect x="16" y="6" width="2" height="14"/><rect x="20" y="3" width="2" height="17"/></g><path d="M1 12 L11 6 L21 1" stroke="#d5143f" stroke-width="1.2" fill="none"/></svg></div>
      <h3 class="feature__title">TITLE HERE</h3>
      <p class="feature__text">Lorem ipsum is simply dummy text of the printing and typesetting industry. Lorem ipsum has been the industry's.</p>
    </div>
    <div class="feature" style="left:151px">
      <div class="feature__icon"><span style="font-family:'Open Sans',sans-serif;font-size:24px;color:var(--red)">$</span></div>
      <h3 class="feature__title">TITLE HERE</h3>
      <p class="feature__text">Lorem ipsum is simply dummy text of the printing and typesetting industry. Lorem ipsum has been the industry's.</p>
    </div>
    <div class="feature" style="left:276px">
      <div class="feature__icon"><svg width="28" height="22" viewBox="0 0 28 22"><g fill="none" stroke="#d5143f"><circle cx="10" cy="13" r="5" stroke-width="3" stroke-dasharray="2.2 1.4"/><circle cx="10" cy="13" r="2" stroke-width="1.5"/><circle cx="21" cy="6" r="3.6" stroke-width="2.5" stroke-dasharray="1.8 1.2"/><circle cx="21" cy="6" r="1.2" stroke-width="1.2"/></g></svg></div>
      <h3 class="feature__title">TITLE HERE</h3>
      <p class="feature__text">Lorem ipsum is simply dummy text of the printing and typesetting industry. Lorem ipsum has been the industry's.</p>
    </div>
    <div class="feature" style="left:403px">
      <div class="feature__icon"><svg width="26" height="24" viewBox="0 0 26 24"><g fill="#d5143f"><rect x="10" y="2" width="15" height="12"/><rect x="2" y="9" width="5" height="8"/><rect x="2" y="17" width="2" height="7"/><rect x="5" y="17" width="2" height="7"/><circle cx="4.5" cy="6" r="2.3"/></g><path d="M13 11 L16 8 L19 10 L22 5" stroke="#fff" stroke-width="1" fill="none"/></svg></div>
      <h3 class="feature__title">TITLE HERE</h3>
      <p class="feature__text">Lorem ipsum is simply dummy text of the printing and typesetting industry. Lorem ipsum has been the industry's.</p>
    </div>
  </div>
  <p class="band-note">Lorem ipsum is simply dummy text of the printing and typesetting industry. It has been the standard placeholder for many years, ever since an unknown printer took a galley of type and scrambled it to make a specimen book. It survived not only many centuries but also the leap into electronic typesetting, remaining essentially unchanged. It was made popular again by transfer lettering sheets and remains in wide use with modern desktop publishing software.</p>
  <div class="brand footer-brand">Tolvik Advisory</div>
  <div class="footer-url">www.tolvikadvisory.se</div>
  <div class="page-no">2</div>
</section>
<div class="label label--icons">Page 02</div>

<section class="slide slide--compare">
  <div class="accent-bar accent-bar--top"></div>
  <h2 class="slide-title">LOREM IPSUM DOLAR</h2>
  <div class="compare-col compare-col--a">
    <h3 class="compare-col__title">TYPE - 1</h3>
    <p class="compare-col__sub">Lorem ipsum is simply dummy text of the printing</p>
    <div class="point"><svg width="8" height="8" viewBox="0 0 8 8"><circle cx="4" cy="4" r="4" fill="#111"/><path d="M2 4.2 L3.5 5.6 L6 2.6" stroke="#fff" stroke-width="1.1" fill="none"/></svg><div class="point__name">POINT 1</div><p class="point__text">Lorem ipsum is simply dummy text of the printing and typesetting industry. Lorem ipsum has been the industry's standard dummy.</p></div>
    <div class="point"><svg width="8" height="8" viewBox="0 0 8 8"><circle cx="4" cy="4" r="4" fill="#111"/><path d="M2 4.2 L3.5 5.6 L6 2.6" stroke="#fff" stroke-width="1.1" fill="none"/></svg><div class="point__name">POINT 2</div><p class="point__text">Lorem ipsum is simply dummy text of the printing and typesetting industry. Lorem ipsum has been the industry's standard dummy.</p></div>
    <div class="point"><svg width="8" height="8" viewBox="0 0 8 8"><circle cx="4" cy="4" r="4" fill="#111"/><path d="M2 4.2 L3.5 5.6 L6 2.6" stroke="#fff" stroke-width="1.1" fill="none"/></svg><div class="point__name">POINT 3</div><p class="point__text">Lorem ipsum is simply dummy text of the printing and typesetting industry. Lorem ipsum has been the industry's standard dummy.</p></div>
    <div class="point"><svg width="8" height="8" viewBox="0 0 8 8"><circle cx="4" cy="4" r="4" fill="#111"/><path d="M2 4.2 L3.5 5.6 L6 2.6" stroke="#fff" stroke-width="1.1" fill="none"/></svg><div class="point__name">POINT 4</div><p class="point__text">Lorem ipsum is simply dummy text of the printing and typesetting industry. Lorem ipsum has been the industry's standard dummy.</p></div>
  </div>
  <div class="compare-col compare-col--b">
    <h3 class="compare-col__title">TYPE - 2</h3>
    <p class="compare-col__sub">Lorem ipsum is simply dummy text of the printing</p>
    <div class="point"><svg width="8" height="8" viewBox="0 0 8 8"><circle cx="4" cy="4" r="4" fill="#111"/><path d="M2 4.2 L3.5 5.6 L6 2.6" stroke="#fff" stroke-width="1.1" fill="none"/></svg><div class="point__name">POINT 1</div><p class="point__text">Lorem ipsum is simply dummy text of the printing and typesetting industry. Lorem ipsum has been the industry's standard dummy.</p></div>
    <div class="point"><svg width="8" height="8" viewBox="0 0 8 8"><circle cx="4" cy="4" r="4" fill="#111"/><path d="M2 4.2 L3.5 5.6 L6 2.6" stroke="#fff" stroke-width="1.1" fill="none"/></svg><div class="point__name">POINT 2</div><p class="point__text">Lorem ipsum is simply dummy text of the printing and typesetting industry. Lorem ipsum has been the industry's standard dummy.</p></div>
    <div class="point"><svg width="8" height="8" viewBox="0 0 8 8"><circle cx="4" cy="4" r="4" fill="#111"/><path d="M2 4.2 L3.5 5.6 L6 2.6" stroke="#fff" stroke-width="1.1" fill="none"/></svg><div class="point__name">POINT 3</div><p class="point__text">Lorem ipsum is simply dummy text of the printing and typesetting industry. Lorem ipsum has been the industry's standard dummy.</p></div>
    <div class="point"><svg width="8" height="8" viewBox="0 0 8 8"><circle cx="4" cy="4" r="4" fill="#111"/><path d="M2 4.2 L3.5 5.6 L6 2.6" stroke="#fff" stroke-width="1.1" fill="none"/></svg><div class="point__name">POINT 4</div><p class="point__text">Lorem ipsum is simply dummy text of the printing and typesetting industry. Lorem ipsum has been the industry's standard dummy.</p></div>
  </div>
  <div class="brand footer-brand">Tolvik Advisory</div>
  <div class="footer-url">www.tolvikadvisory.se</div>
  <div class="page-no">3</div>
</section>
<div class="label label--compare">Page 03</div>

</body>
</html>
```